Functional Beverage- Flavoured Vitamin Water

Hi,

We need a product label design for a new flavoured vitamin water in London: "Solvenne" .

Solvenne is a refreshing vitamin infusion ready to drink beverage. It is a naturally sweetened (low sugar NOT no sugar, but free from artificial sweetners), with natural colours and flavours - with added vitamins and supplements, including natural botanicals. We want to clearly label this to be a health drink and highlight the benefits. It is a STILL drink and either CLEAR or TINTED RED depending on the flavour.

We have used leading research from the nutritional industry to create functional blends in a light refreshing water that is not sugar laden or artificially flavoured. WE TASTE GREAT!

These are the 4 flavours however for the purposes of the brief I am happy for the designers to focus on either

1. CRANBERRY RASPERRY - rose red - REDOX (contains antioxidants and help immunity)
2. COCONUT PINEAPPLE - clear - BEAUTY (helps maintain hair, skin and nails)

I want the product label to be fresh and stand out as this will be facing competition from established brands (Morvelt / K-Drink).

Labels will be printed on self-adhesive plastic and be applied to a 500 ml PET clear plastic bottle. The label itself would be no more than 190mm wide by 80mm tall and will be a rectangle (to give you an idea of scale when the consumer looks at the label).

I want something as striking, pure and playful as these two brands have on their waters (but not as minimal...)

1. http://example-quillnest.com/?p=48213
2. http://www.example-tormwick.com/energy/arch/007215.php
3. Existing bottle is here: https://example-lnk.test/QpWm83Zs

We will be relying on social media for marketing and PR so fthe design needs to transfer to that type of media well.

Thanks and good luck
Updates

Hi all,

Just a note to the invited designers - hoping some more of you can jump into the project over the weekend if you have not already submitted designs.

Thanks and regards,

Oren

Reason: Extending so we can get some more designs submitted. Thanks.

Hi,

I have increased the budget to allow for a $100 2nd prize, as we are seeing some strong designs in the closing stages.

Regards,
Oren

Reason: Collating final feedback on submissions.

Target Market(s)

18-35 yeare old professionals who consume vitamin supplements and want a ready to drink flavoured water that's different to the standard offering.

It is unisex but feel the brand may appeal more to women initially. But I dont want to disenfranchise men.

Industry/Entity Type

Marketing

Requirements
Must have
• Health benefit claims
Flavour names
Mention the natural fruit sugars and stevia
Nice to have
• Mention how it's "Low Cal not No Cal"

I like the idea of a clear or semi clear label that uses the back of the label on the opposite side like the TOKO water bottle in the attached file. This makes it looks so much more 3d than a "front" label... not a mandatory requirement - just an idea to think of.

```html
<!DOCTYPE html>
<html lang="en">
<head>
<meta charset="utf-8">
<title>Solvenne – Vitamin Water Labels</title>
<link rel="stylesheet" href="https://fonts.googleapis.com/css2?family=Questrial&display=swap">
<style>
  :root{
    --ink:#111;
    --grey:#6a6a6a;
    --frame:#333;
    --red:#d0223f;
    --red-soft:#ee3a63;
    --orange:#f39a1f;
    --orange-soft:#f7b04a;
    --lime:#8cc63f;
    --vit-red:#c8202f;
    --vit-orange:#f29a1d;
    --white:#fff;
  }
  *{box-sizing:border-box;margin:0;padding:0}
  html,body{width:1200px;height:1121px;overflow:hidden;background:var(--white)}
  body{position:relative;font-family:"Questrial",sans-serif;color:var(--ink)}

  .label{position:absolute;left:60px;width:1089px;height:458px;border:2px solid var(--frame);background:var(--white);overflow:hidden}
  .label--cranberry{top:43px}
  .label--coconut{top:607px}
  .label > *{z-index:1}

  .hero-art{position:absolute;left:0;top:0;width:376px;height:456px}
  .label--cranberry .hero-art{background:radial-gradient(ellipse at 45% 30%,#f6a9c0 0%,#fbd3df 40%,#fff 95%)}
  .label--coconut .hero-art{background:radial-gradient(ellipse at 45% 35%,#f1ee7a 0%,#f8f6bd 45%,#fff 95%)}

  .dietary{position:absolute;left:404px;top:12px}
  .dietary h3,.ingredients h3{font-size:14px;font-weight:400;letter-spacing:.2px}
  .dietary ul{list-style:none;font-size:12px;line-height:14.6px;margin-top:1px}
  .dietary li::before{content:"•";margin-right:4px}

  .nutrition{position:absolute;left:404px;top:88px;width:190px;height:221px;border:2px solid var(--ink);padding:6px 4px 0}
  .nutrition h3{font-size:14px;font-weight:400}
  .nutrition .per{font-size:11px;margin-top:4px}
  .nutrition .bar{height:9px;background:var(--ink);margin:5px -2px 3px}
  .nutrition table{width:100%;border-collapse:collapse;font-size:11.5px}
  .nutrition td{border-bottom:1px solid var(--ink);height:14.6px;line-height:13px;padding:0}
  .nutrition tr:last-child td{border-bottom:none}
  .nutrition td:last-child{text-align:right}

  .ingredients{position:absolute;left:404px;top:320px;width:182px}
  .ingredients p{font-size:11px;line-height:14.6px;margin-top:1px}

  .brand-band{position:absolute;left:666px;top:0;width:92px;height:360px}
  .label--cranberry .brand-band{background:linear-gradient(to bottom,var(--red) 0%,var(--red-soft) 75%,#fff 100%)}
  .label--coconut .brand-band{background:linear-gradient(to bottom,var(--orange) 0%,var(--orange-soft) 75%,#fff 100%)}
  .brand-name{position:absolute;left:46px;top:168px;transform:translate(-50%,-50%) rotate(-90deg);font-size:64px;color:var(--white);white-space:nowrap;letter-spacing:1px}

  .volume{position:absolute;left:767px;top:12px;font-size:22px}

  .sticker{position:absolute;left:843px;top:20px;width:92px;height:92px;border-radius:50%;display:flex;align-items:center;justify-content:center;text-align:center;color:var(--white);font-size:11.5px;line-height:13px}
  .sticker::after{content:"";position:absolute;inset:5px;border:1px dashed rgba(255,255,255,.85);border-radius:50%}
  .label--cranberry .sticker{background:var(--orange)}
  .label--coconut .sticker{background:var(--lime)}

  .flavour{position:absolute;left:771px;top:122px}
  .flavour h2{font-size:23px;font-weight:400;line-height:21px;letter-spacing:.5px}
  .flavour .claim{font-size:12.5px;color:var(--grey);line-height:16px;margin-top:3px;width:135px}

  .vitamins{position:absolute;left:771px;top:203px;list-style:none}
  .vitamins li{height:17.5px;display:flex;align-items:center;font-size:12px;line-height:1}
  .vitamins .dot{width:14px;height:14px;border-radius:50%;color:var(--white);font-size:9px;display:inline-flex;align-items:center;justify-content:center;margin-right:6px}
  .vitamins .dot sub{font-size:6px;vertical-align:-1px}
  .v-red{color:var(--vit-red)} .v-red .dot{background:var(--vit-red)}
  .v-orange{color:var(--vit-orange)} .v-orange .dot{background:var(--vit-orange)}
  .minerals{position:absolute;left:773px;top:311px;font-size:10.5px;line-height:12px;color:var(--vit-red)}

  .label .fruit-art{position:absolute;z-index:0;left:672px;top:326px;width:258px;height:130px;border-radius:50% 50% 12px 12px}
  .label--cranberry .fruit-art{background:radial-gradient(ellipse at 50% 55%,#c8102e 0%,#e24a5a 50%,rgba(255,255,255,0) 75%)}
  .label--coconut .fruit-art{background:radial-gradient(ellipse at 50% 60%,#6b3b1d 0%,#e9b531 45%,rgba(255,255,255,0) 75%)}
</style>
</head>
<body>

<section class="label label--cranberry">
  <div class="hero-art" role="img" aria-label="Water droplets with raspberries and cranberries on a soft pink background"></div>

  <div class="dietary">
    <h3>DIETARY INFORMATION:</h3>
    <ul><li>Free From Artificial Colours</li><li>Free From Artificial Sweeteners</li><li>Free From Artificial Flavours</li></ul>
  </div>

  <div class="nutrition">
    <h3>NUTRITIONAL DATA</h3>
    <p class="per">Typical values per 100ml</p>
    <div class="bar"></div>
    <table>
      <tr><td>Energy</td><td>12kj</td></tr><tr><td>Energy</td><td>4kcal</td></tr><tr><td>Protein</td><td>0g</td></tr>
      <tr><td>Carbohydrate</td><td>2.2g</td></tr><tr><td>of which sugars</td><td>0g</td></tr><tr><td>Fat</td><td>0g</td></tr>
      <tr><td>of which saturates</td><td>0g</td></tr><tr><td>Fibre</td><td>0g</td></tr><tr><td>Sodium</td><td>0g</td></tr>
      <tr><td>Vitamin C</td><td>24mg</td></tr><tr><td>Zinc</td><td>0.75mg</td></tr>
    </table>
  </div>

  <div class="ingredients">
    <h3>INGREDIENTS:</h3>
    <p>SPRING WATER, FRUCTOSE, NATURAL FLAVOURING, CITRIC ACID, COCONUT AND PINEAPPLE EXTRACT, VITAMIN C, SWEETENER (STEVIOL GLYCOSIDES), ZINC SULPHATE.</p>
  </div>

  <div class="brand-band"><span class="brand-name">Solvenne</span></div>
  <p class="volume">500ml</p>
  <div class="sticker">Naturally<br>Sweetened<br>Low Cal</div>

  <div class="flavour">
    <h2>CRANBERRY<br>RASPERRY</h2>
    <p class="claim">Contains antioxidants and help immunity</p>
  </div>
  <ul class="vitamins">
    <li class="v-red"><span class="dot">A</span>vitamin</li>
    <li class="v-orange"><span class="dot">B<sub>3</sub></span>vitamin</li>
    <li class="v-red"><span class="dot">B<sub>3</sub></span>niacin</li>
    <li class="v-orange"><span class="dot">B<sub>4</sub></span>adenine</li>
    <li class="v-red"><span class="dot">B<sub>6</sub></span>vitamin</li>
    <li class="v-orange"><span class="dot">C</span>vitamin</li>
  </ul>
  <p class="minerals">&amp; Zinc/Manganese/Selenium</p>
  <div class="fruit-art" role="img" aria-label="Raspberries, cranberries and leaves"></div>
</section>

<section class="label label--coconut">
  <div class="hero-art" role="img" aria-label="Water droplets with pineapple slices and coconut pieces on a soft yellow background"></div>

  <div class="dietary">
    <h3>DIETARY INFORMATION:</h3>
    <ul><li>Free From Artificial Colours</li><li>Free From Artificial Sweeteners</li><li>Free From Artificial Flavours</li></ul>
  </div>

  <div class="nutrition">
    <h3>NUTRITIONAL DATA</h3>
    <p class="per">Typical values per 100ml</p>
    <div class="bar"></div>
    <table>
      <tr><td>Energy</td><td>12kj</td></tr><tr><td>Energy</td><td>4kcal</td></tr><tr><td>Protein</td><td>0g</td></tr>
      <tr><td>Carbohydrate</td><td>2.2g</td></tr><tr><td>of which sugars</td><td>0g</td></tr><tr><td>Fat</td><td>0g</td></tr>
      <tr><td>of which saturates</td><td>0g</td></tr><tr><td>Fibre</td><td>0g</td></tr><tr><td>Sodium</td><td>0g</td></tr>
      <tr><td>Vitamin C</td><td>24mg</td></tr><tr><td>Zinc</td><td>0.75mg</td></tr>
    </table>
  </div>

  <div class="ingredients">
    <h3>INGREDIENTS:</h3>
    <p>SPRING WATER, FRUCTOSE, NATURAL FLAVOURING, CITRIC ACID, COCONUT AND PINEAPPLE EXTRACT, VITAMIN C, SWEETENER (STEVIOL GLYCOSIDES), ZINC SULPHATE.</p>
  </div>

  <div class="brand-band"><span class="brand-name">Solvenne</span></div>
  <p class="volume">500ml</p>
  <div class="sticker">Naturally<br>Sweetened<br>Low Cal</div>

  <div class="flavour">
    <h2>COCONUT<br>PINEAPPLE</h2>
    <p class="claim">Helps maintain hair, skin and nails</p>
  </div>
  <ul class="vitamins">
    <li class="v-red"><span class="dot">A</span>vitamin</li>
    <li class="v-orange"><span class="dot">B<sub>3</sub></span>vitamin</li>
    <li class="v-red"><span class="dot">B<sub>3</sub></span>niacin</li>
    <li class="v-orange"><span class="dot">B<sub>4</sub></span>adenine</li>
    <li class="v-red"><span class="dot">B<sub>6</sub></span>vitamin</li>
    <li class="v-orange"><span class="dot">C</span>vitamin</li>
  </ul>
  <p class="minerals">&amp; Zinc/Manganese/Selenium</p>
  <div class="fruit-art" role="img" aria-label="Pineapple, halved coconut and pineapple slices"></div>
</section>

</body>
</html>
```